I need the following on my business card:
- Name: Dana Whitcomb
- License # 0M93216
- Title: Producer
- Phone: (555) 017-3904
- Email: Dana@CorbelInsuranceServices.com

- Company: Corbel Insurance Services
- Address: 27408 Larkmoor Ave Suite 610, Fenwick Hollow, CA 90217
- Website: www.CorbelInsuranceServices.com

Also add our slogan on the card: "Where Care Meets Protection"

```html
<!DOCTYPE html>
<html lang="en">
<head>
<meta charset="utf-8">
<title>Corbel Insurance Services – Business Card</title>
<link rel="stylesheet" href="https://fonts.googleapis.com/css2?family=Roboto:wght@400;500;700&display=swap">
<style>
  :root {
    --navy: #1f2866;
    --green: #178a3a;
    --card-white: #f2f2f2;
    --backdrop: #e3e5e4;
    --silver: #e6e6e6;
  }
  * { margin: 0; padding: 0; box-sizing: border-box; }
  html, body {
    width: 1200px; height: 1200px; overflow: hidden;
    background: var(--backdrop);
    font-family: "Roboto", Arial, sans-serif;
  }
  .sheet { position: relative; width: 1200px; height: 1200px; }
  .card {
    position: absolute; left: 160px; width: 880px; height: 503px;
    border-radius: 4px;
  }
  .card-front { top: 62px; background: var(--card-white); }
  .card-back { top: 635px; background: var(--navy); }

  .line {
    position: absolute; left: 83px; height: 32px; line-height: 32px;
    white-space: nowrap; color: var(--navy); font-size: 24px;
  }
  .holder-name { top: 75px; height: 40px; line-height: 40px; color: var(--green); font-weight: 700; font-size: 37px; letter-spacing: -0.6px; }
  .holder-title { top: 113px; font-size: 25px; }
  .holder-license { top: 144px; color: var(--green); font-size: 25px; }

  .company-name { top: 234px; color: var(--green); font-weight: 700; font-size: 27px; }
  .address-1 { top: 269px; }
  .address-2 { top: 300px; }

  .contact { display: flex; align-items: center; gap: 10px; }
  .contact-phone { top: 342px; }
  .contact-email { top: 371px; }
  .contact-web { top: 399px; }
  .contact svg { width: 19px; height: 19px; flex: none; fill: var(--green); }

  .brand-front {
    position: absolute; left: 536px; width: 262px; top: 88px;
    color: var(--navy); font-weight: 700; text-align: center;
  }
  .brand-front .brand-word { display: block; font-size: 50px; line-height: 56px; letter-spacing: 1px; }
  .brand-front .brand-sub { display: block; font-size: 17px; line-height: 26px; letter-spacing: 4px; margin-right: -4px; }

  .brand-back {
    position: absolute; left: 0; right: 0; top: 190px; text-align: center;
    color: var(--silver); font-weight: 700;
  }
  .brand-back .brand-word { display: block; font-size: 96px; line-height: 104px; letter-spacing: 3px; }
  .brand-back .brand-sub { display: block; font-size: 30px; line-height: 44px; letter-spacing: 10px; margin-right: -10px; }
  .slogan {
    position: absolute; left: 0; right: 0; top: 428px; text-align: center;
    color: var(--silver); font-weight: 500; font-size: 23px; line-height: 32px;
  }
</style>
</head>
<body>
<main class="sheet">
  <section class="card card-front">
    <div class="line holder-name">Dana Whitcomb</div>
    <div class="line holder-title">Producer</div>
    <div class="line holder-license">License # 0M93216</div>

    <div class="brand-front">
      <span class="brand-word">CORBEL</span>
      <span class="brand-sub">INSURANCE SERVICES</span>
    </div>

    <div class="line company-name">Corbel Insurance Services</div>
    <div class="line address-1">27408 Larkmoor Ave Suite 610,</div>
    <div class="line address-2">Fenwick Hollow, CA 90217</div>

    <div class="line contact contact-phone">
      <svg viewBox="0 0 24 24" aria-hidden="true"><path d="M6.6 10.8a15.1 15.1 0 0 0 6.6 6.6l2.2-2.2c.3-.3.7-.4 1-.2 1.1.4 2.3.6 3.6.6.6 0 1 .4 1 1V20c0 .6-.4 1-1 1A17 17 0 0 1 3 4c0-.6.4-1 1-1h3.5c.6 0 1 .4 1 1 0 1.3.2 2.5.6 3.6.1.3 0 .7-.2 1z"/></svg>
      (555) 017-3904
    </div>
    <div class="line contact contact-email">
      <svg viewBox="0 0 24 24" aria-hidden="true"><path d="M2 5h20v2l-10 6L2 7z"/><path d="M2 9l10 6 10-6v10H2z"/></svg>
      Dana@CorbelInsuranceServices.com
    </div>
    <div class="line contact contact-web">
      <svg viewBox="0 0 24 24" aria-hidden="true"><circle cx="12" cy="12" r="10"/><path d="M2 12h20M12 2c3 3 3 17 0 20M12 2c-3 3-3 17 0 20" stroke="#f2f2f2" stroke-width="1.6" fill="none"/></svg>
      www.CorbelInsuranceServices.com
    </div>
  </section>

  <section class="card card-back">
    <div class="brand-back">
      <span class="brand-word">CORBEL</span>
      <span class="brand-sub">INSURANCE SERVICES</span>
    </div>
    <div class="slogan">"Where Care Meets Protection"</div>
  </section>
</main>
</body>
</html>
```